Business cards for Pine Ridge Timber Homes
Hal R. Denton Jr. / 2nd card is for Marla Denton
Business cards for Pine Ridge Timber Homes  - Construction
Creative Brief
Simple
Hal R. Denton Jr. for one card / Marla Denton for another card
No titles needed
No physical address needed on the card
Hal's Cell number is 555-317-6048, Serena's cell number is 555-317-8391
pine.ridge@mailbox-example.com
www.pineridgeexample.com
No license needed
Our preference is to see the logo on the front of the card and name and contact information on the back but we are open to whatever design ideas you can come up with.
hdenton4823 hdenton4823
We are getting closer now. Thanks for your extra efforts to show us a few more things. On #175: On the front- We would like for you to move the name straight up on the card just a little so that you have room to make the phone numbers, email address, and web address font just a little bit bigger and therefore easier to read. We think the phone numbers, email address, and web address should remain smaller than my name on the card and we like that there is a little separation vertically between my name and the contact information pieces. We are not looking for a radical change in font sizes here. We would like to see a subtle change that makes the contact information just a little more clear. On the back- the only change we would like to see is that the "www.pineridgeexample.com" text would be changed to black instead of the gray it currently is. This version is a winner for us once we get these minor changes done. If you would post the other version we need for Marla Denton too that would be great. Thanks
On #167 we would like to see the logo from #157. You would also need to change colors on the front of the card to match the new logo. Thanks
On #151, we would like to see versions that are not on a transparent card. One where the area behind the logo is white and another where the area behind the logo is our preferred crème (red 250, green 227, blue 172). Thanks
On #132 there is shadow of the logo on the transparent section surrounding the full color logo. Is it possible to create the same effect on #133 in the white area surrounding the full color logo?
We would like to see number #84 where the white on both sides of the card is replaced with a crème color (red 250,green 227, blue 172)

```html
<!DOCTYPE html>
<html lang="en">
<head>
<meta charset="utf-8">
<title>Pine Ridge Timber Homes — Business Cards</title>
<link rel="stylesheet" href="https://fonts.googleapis.com/css2?family=Open+Sans:wght@400;600;700&display=swap">
<style>
  :root {
    --stage: #2b2b2c;
    --creme: #fae3ac;
    --creme-light: #fcebc4;
    --bark: #2a1c14;
    --tan: #d9a35f;
    --ink: #1c140f;
    --text-light: #f4ece0;
  }
  * { box-sizing: border-box; margin: 0; padding: 0; }
  html, body {
    width: 1200px; height: 750px; overflow: hidden;
    background: var(--stage);
    font-family: "Open Sans", sans-serif;
  }
  .sheet { position: relative; width: 1200px; height: 750px; }
  .card {
    position: absolute; top: 129px;
    width: 281px; height: 492px;
    background: linear-gradient(90deg, var(--creme) 0%, var(--creme-light) 100%);
    overflow: hidden;
  }
  .card--hal { left: 122px; }
  .card--marla { left: 460px; }
  .card--back { left: 802px; }
  .card__shape { position: absolute; inset: 0; width: 100%; height: 100%; }
  .brand {
    position: absolute; left: 0; right: 0;
    text-align: center;
    font-weight: 700; font-size: 24px; letter-spacing: 0.5px;
    color: var(--bark);
  }
  .card--hal .brand, .card--marla .brand { top: 80px; padding-left: 56px; }
  .card--back .brand { top: 230px; }
  .person {
    position: absolute; left: 26px; top: 366px;
    color: var(--text-light);
  }
  .person__name { font-size: 18px; font-weight: 600; margin-bottom: 14px; }
  .contact { list-style: none; }
  .contact__item {
    display: flex; align-items: center;
    height: 20.5px; font-size: 12.5px;
  }
  .contact__icon { width: 12px; height: 12px; margin-right: 8px; flex: none; fill: var(--text-light); }
  .back-url {
    position: absolute; left: 0; right: 0; top: 419px;
    text-align: center; font-size: 11.5px; letter-spacing: 1.6px;
    color: var(--ink);
  }
</style>
</head>
<body>
<main class="sheet">

  <section class="card card--hal" aria-label="Front card, Hal R. Denton Jr.">
    <svg class="card__shape" viewBox="0 0 300 525" preserveAspectRatio="none" aria-hidden="true">
      <path d="M0,160 C80,290 190,346 300,349 L300,384 C170,372 60,282 0,164 Z" fill="var(--tan)"/>
      <path d="M0,164 C60,282 170,372 300,384 L300,525 L0,525 Z" fill="var(--bark)"/>
    </svg>
    <div class="brand">Pine Ridge</div>
    <div class="person">
      <h2 class="person__name">Hal R. Denton Jr.</h2>
      <ul class="contact">
        <li class="contact__item"><svg class="contact__icon" viewBox="0 0 12 12"><path d="M3,0h6a1,1 0 0 1 1,1v10a1,1 0 0 1-1,1H3a1,1 0 0 1-1-1V1a1,1 0 0 1 1-1zM3.5,1.5v8h5v-8z"/></svg>555-317-6048</li>
        <li class="contact__item"><svg class="contact__icon" viewBox="0 0 12 12"><path d="M0,4 C0,1 12,1 12,4 L10,5 L8.5,3.5 L3.5,3.5 L2,5Z M2,6 L4,4.5 L8,4.5 L10,6 L10,11 L2,11Z"/></svg>555-204-7730 (TF)</li>
        <li class="contact__item"><svg class="contact__icon" viewBox="0 0 12 12"><path d="M0,2h12v1L6,7L0,3z M0,4.5L6,8.5L12,4.5V10H0z"/></svg>pine.ridge@mailbox-example.com</li>
        <li class="contact__item"><svg class="contact__icon" viewBox="0 0 12 12"><path d="M6,0.5a5.5,5.5 0 1 0 0.01,0z M6,1.6c-1,1.2-1.5,2.6-1.5,4.4s.5,3.2,1.5,4.4c1-1.2,1.5-2.6,1.5-4.4S7,2.8,6,1.6z M1.7,5.5h8.6v1H1.7z" fill-rule="evenodd"/></svg>www.pineridgeexample.com</li>
      </ul>
    </div>
  </section>

  <section class="card card--marla" aria-label="Front card, Marla Denton">
    <svg class="card__shape" viewBox="0 0 300 525" preserveAspectRatio="none" aria-hidden="true">
      <path d="M0,160 C80,290 190,346 300,349 L300,384 C170,372 60,282 0,164 Z" fill="var(--tan)"/>
      <path d="M0,164 C60,282 170,372 300,384 L300,525 L0,525 Z" fill="var(--bark)"/>
    </svg>
    <div class="brand">Pine Ridge</div>
    <div class="person">
      <h2 class="person__name">Marla Denton</h2>
      <ul class="contact">
        <li class="contact__item"><svg class="contact__icon" viewBox="0 0 12 12"><path d="M3,0h6a1,1 0 0 1 1,1v10a1,1 0 0 1-1,1H3a1,1 0 0 1-1-1V1a1,1 0 0 1 1-1zM3.5,1.5v8h5v-8z"/></svg>555-317-8391</li>
        <li class="contact__item"><svg class="contact__icon" viewBox="0 0 12 12"><path d="M0,4 C0,1 12,1 12,4 L10,5 L8.5,3.5 L3.5,3.5 L2,5Z M2,6 L4,4.5 L8,4.5 L10,6 L10,11 L2,11Z"/></svg>555-204-7730 (TF)</li>
        <li class="contact__item"><svg class="contact__icon" viewBox="0 0 12 12"><path d="M0,2h12v1L6,7L0,3z M0,4.5L6,8.5L12,4.5V10H0z"/></svg>pine.ridge@mailbox-example.com</li>
        <li class="contact__item"><svg class="contact__icon" viewBox="0 0 12 12"><path d="M6,0.5a5.5,5.5 0 1 0 0.01,0z M6,1.6c-1,1.2-1.5,2.6-1.5,4.4s.5,3.2,1.5,4.4c1-1.2,1.5-2.6,1.5-4.4S7,2.8,6,1.6z M1.7,5.5h8.6v1H1.7z" fill-rule="evenodd"/></svg>www.pineridgeexample.com</li>
      </ul>
    </div>
  </section>

  <section class="card card--back" aria-label="Back card">
    <div class="brand">Pine Ridge</div>
    <p class="back-url">www.pineridgeexample.com</p>
  </section>

</main>
</body>
</html>
```